u-vanta Business Card Design Project

I need a freshening of an exisiting logo and that fresh look placed on an exisiting business card layout. That layout is attached along with the exisiting logo in use. The sample business card i am attaching is for our holding company "plume ledger". The logo needed on the card is the u-vanta logo which is our brand. you can go to our website uvanta.com to see various uses of the logo as we use it today. The front and back of the card should be looked at. The test edits to the card are:
websit: should be uvanta.com
address: should be 218 w marlowe suite #207 Brenton, Nv. 50312
all other content is the same.

This is my first attempt with draft kiosk, thank you for your help. I have many more projects needing graphic work so hopefully this is my solution.

Target Market(s)

Business to Business customers see our website uvanta.com

Industry/Entity Type

Business

Requirements
Must have
• leave look similar just freshen the uvanta logo,

```html
<!DOCTYPE html>
<html lang="en">
<head>
<meta charset="utf-8">
<title>u-vanta business card</title>
<link rel="stylesheet" href="https://fonts.googleapis.com/css2?family=Didact+Gothic&display=swap">
<style>
  :root {
    --backdrop: #2a2a2a;
    --card: #ffffff;
    --card-shade: #ececec;
    --ink: #3a3a3a;
    --ink-soft: #555555;
    --accent: #7aae2c;
    --band-top: #86b43a;
    --band-bottom: #6f9f28;
    --rule: #777777;
  }
  * { box-sizing: border-box; margin: 0; padding: 0; }
  html, body {
    width: 1200px; height: 900px; overflow: hidden;
    background: var(--backdrop);
    font-family: "Didact Gothic", "Century Gothic", sans-serif;
    color: var(--ink);
  }
  .sheet { position: relative; width: 1200px; height: 900px; }
  .card {
    position: absolute; left: 250px; width: 700px; height: 400px;
    background: linear-gradient(135deg, var(--card) 55%, var(--card-shade));
    overflow: hidden;
  }
  .card--back { top: 40px; }
  .card--front { top: 460px; }

  .side-band {
    position: absolute; top: 0; right: 0; width: 92px; height: 400px;
    background: linear-gradient(180deg, var(--band-top), var(--band-bottom));
  }

  .brand { display: flex; align-items: center; gap: 10px; color: var(--ink); }
  .brand-dot { width: 14px; height: 14px; border-radius: 50%; background: var(--accent); }
  .card--back .brand { position: absolute; left: 150px; top: 120px; font-size: 64px; }
  .card--back .brand-dot { width: 22px; height: 22px; }
  .card--front .brand { position: absolute; left: 40px; top: 34px; font-size: 36px; }

  .tagline {
    position: absolute; border: 1px solid var(--rule); border-radius: 12px;
    padding: 3px 14px; color: var(--ink); white-space: nowrap;
  }
  .card--back .tagline { left: 210px; top: 226px; font-size: 22px; padding: 5px 18px; border-radius: 18px; }
  .card--front .tagline { left: 340px; top: 42px; font-size: 14px; }

  .website { position: absolute; left: 0; right: 92px; text-align: center; color: var(--ink); }
  .card--back .website { bottom: 34px; font-size: 26px; }
  .card--front .website { bottom: 26px; font-size: 22px; }

  .person { position: absolute; left: 60px; top: 140px; }
  .person-name { font-size: 24px; letter-spacing: 0.5px; }
  .person-role { font-size: 15px; color: var(--ink-soft); margin: 8px 0 0 36px; }

  .contact-list { position: absolute; left: 70px; top: 250px; list-style: none; }
  .contact-list li { display: flex; align-items: center; gap: 20px; font-size: 15px; margin-bottom: 22px; }
  .contact-list svg { width: 18px; height: 18px; }

  .address { position: absolute; left: 420px; top: 126px; font-size: 16px; line-height: 1.25; color: var(--ink-soft); font-style: normal; }
</style>
</head>
<body>
<main class="sheet">

  <section class="card card--back" aria-label="Card back">
    <div class="side-band" role="img" aria-label="Decorative measuring-scale band in brand colours"></div>
    <div class="brand"><span class="brand-dot"></span><span class="brand-name">u-vanta</span></div>
    <p class="tagline">What story does your name tell?</p>
    <p class="website">www.uvanta.com</p>
  </section>

  <section class="card card--front" aria-label="Card front">
    <div class="side-band" role="img" aria-label="Decorative measuring-scale band in brand colours"></div>
    <div class="brand"><span class="brand-dot"></span><span class="brand-name">u-vanta</span></div>
    <p class="tagline">What story does your name tell?</p>

    <div class="person">
      <p class="person-name">Daniel R. Whitfield</p>
      <p class="person-role">VP of Distribution</p>
    </div>

    <ul class="contact-list">
      <li>
        <svg viewBox="0 0 18 18" aria-label="Mobile"><rect x="5" y="1.5" width="8" height="15" rx="1.5" fill="none" stroke="var(--ink)" stroke-width="1.3"/><line x1="8" y1="14" x2="10" y2="14" stroke="var(--ink)" stroke-width="1.3"/></svg>
        <span>+001 555 018</span>
      </li>
      <li>
        <svg viewBox="0 0 18 18" aria-label="Phone"><circle cx="9" cy="9" r="7.5" fill="none" stroke="var(--ink)" stroke-width="1.3"/><path d="M6.5 5.5c-1 1.5 0 4 1.5 5.5s3.5 2.5 5 1.5l-1.2-1.5-1.3.6c-1-.5-2-1.5-2.5-2.5l.6-1.3z" fill="var(--ink)"/></svg>
        <span>+001 555 018</span>
      </li>
    </ul>

    <address class="address">u-vanta<br>218 w marlowe suite<br>#207 Brenton,<br>Nv. 50312</address>

    <p class="website">www.uvanta.com</p>
  </section>

</main>
</body>
</html>
```